Re-style home page - eye-catching and unique design for social commerce website

We need a new concept design for TrindaMo's home page.
We don't want to make huge changes but creating a more professional and eye-catching style.

We need to look very serious like a professional services company and in the same time to look like a social network for e-commerce.

Our logo is very captive and you can use to creating something of harmonious.

This is a re-style and I'm excepted to see unique and fresh design like Clovaret.

Target Market(s)

e-commerce and social

Industry/Entity Type

Social

Number of Pages Required

1 page

Font styles to use
Serif
Sans Serif

Requirements
Must have
• An eye-catching result.
• Search bar with logo and Login How it works and business
• The slogan with login and signup.
• Footer links.
Nice to have
• I would like to open the home page and see only two clear ways:
• -Consumer
• --Search
• --The slogan
• --Login and Signup
• --How it works
• -Business
• --Go to Business area
• Background: City, Shopping.
Should not have
• Scrollbar style!

```html
<!DOCTYPE html>
<html lang="en">
<head>
<meta charset="utf-8">
<title>TrindaMo – How It Works</title>
<link rel="stylesheet" href="https://fonts.googleapis.com/css2?family=Roboto:wght@300;400;500&display=swap">
<style>
  :root {
    --ink: #474c51;
    --text: #5d6165;
    --muted: #6b6e71;
    --accent: #f5b400;
    --band: #f0f0f0;
    --page: #ffffff;
    --tab: #2b2f33;
    --frame: #dcdcdc;
  }
  * { box-sizing: border-box; margin: 0; padding: 0; }
  html, body { width: 1200px; height: 1004px; overflow: hidden; background: var(--page); }
  body { position: relative; font-family: "Roboto", "Helvetica Neue", Arial, sans-serif; color: var(--text); font-weight: 300; }

  .support-tab {
    position: absolute; left: 0; top: 130px; width: 33px; height: 126px;
    background: var(--tab); border-radius: 0 3px 3px 0;
    display: flex; flex-direction: column; align-items: center; justify-content: center; gap: 6px;
  }
  .support-tab__label {
    writing-mode: vertical-rl; color: #fff; font-size: 13px; font-weight: 500; letter-spacing: .3px;
  }
  .support-tab__dot { width: 10px; height: 10px; border-radius: 50%; background: var(--accent); }

  .how-it-works { position: absolute; left: 0; top: 0; width: 1200px; height: 418px; }
  .how-it-works__title {
    position: absolute; top: 69px; width: 100%; text-align: center;
    font-size: 20px; font-weight: 500; color: var(--ink);
  }
  .how-it-works__intro {
    position: absolute; top: 105px; width: 100%; text-align: center;
    font-size: 18px; line-height: 27px; color: var(--muted);
  }

  .step { position: absolute; }
  .step__icon { position: absolute; }
  .step__title { position: absolute; white-space: nowrap; font-size: 20px; font-weight: 300; color: var(--ink); }
  .step__body { position: absolute; white-space: nowrap; font-size: 13px; line-height: 20.5px; color: var(--muted); }

  .step--signup .step__icon { left: 228px; top: 248px; }
  .step--signup .step__title { left: 305px; top: 230px; }
  .step--signup .step__body { left: 305px; top: 261px; }

  .step--interests .step__icon { left: 654px; top: 242px; }
  .step--interests .step__title { left: 740px; top: 227px; }
  .step--interests .step__body { left: 740px; top: 258px; }

  .experience { position: absolute; left: 0; top: 418px; width: 1200px; height: 355px; background: var(--band); }
  .experience__title { position: absolute; left: 229px; top: 96px; font-size: 20px; font-weight: 500; color: var(--ink); }
  .experience__body { position: absolute; left: 229px; top: 131px; font-size: 18px; line-height: 27px; color: var(--muted); }
  .video {
    position: absolute; left: 668px; top: 45px; width: 382px; height: 256px;
    border: 3px solid var(--frame);
    background: linear-gradient(135deg, #6a4a36 0%, #3a2a22 40%, #2a2624 65%, #7a5c48 100%);
  }
  .video__play {
    position: absolute; left: 156px; top: 98px; width: 83px; height: 49px;
    background: var(--accent); border-radius: 2px; opacity: .92;
    display: flex; align-items: center; justify-content: center;
  }

  .business { position: absolute; left: 0; top: 773px; width: 1200px; height: 231px; }
  .business__people { position: absolute; left: 208px; top: 100px; width: 404px; height: 140px; }
  .business__portrait { position: absolute; border-radius: 50%; border: 4px solid #e8e8e8; }
  .business__portrait--left { left: 0; top: 20px; width: 140px; height: 140px; background: linear-gradient(160deg, #c9a58a, #7d8aa0); }
  .business__portrait--right { left: 262px; top: 20px; width: 140px; height: 140px; background: linear-gradient(160deg, #e0c8b4, #b9a592); }
  .business__portrait--center { left: 100px; top: 0; width: 210px; height: 210px; background: linear-gradient(160deg, #8b8074, #5a5048 60%, #a79c90); }
  .business__title { position: absolute; left: 679px; top: 88px; font-size: 20px; font-weight: 500; color: var(--ink); }
  .business__body { position: absolute; left: 679px; top: 123px; font-size: 18px; line-height: 27px; color: var(--muted); white-space: nowrap; }
</style>
</head>
<body>
  <aside class="support-tab">
    <span class="support-tab__label">Get Support</span>
    <span class="support-tab__dot"></span>
  </aside>

  <section class="how-it-works">
    <h2 class="how-it-works__title">How It Works</h2>
    <p class="how-it-works__intro">We offer an innovative way of shopping<br>Ut enim ad minim veniam, quis nostrud exercitation ullamco laboris.</p>

    <div class="step step--signup">
      <svg class="step__icon" width="64" height="58" viewBox="0 0 64 58" fill="none">
        <path d="M1 1h36l6 6v49H1z" stroke="#474c51" stroke-width="1.6"/>
        <path d="M7 12h22M7 19h26M7 26h20M7 33h24M7 40h18M7 47h22" stroke="#474c51" stroke-width="1.4"/>
        <circle cx="46" cy="26" r="5.5" stroke="#f5b400" stroke-width="1.6"/>
        <path d="M36 42c1-6 5-9 10-9s9 3 10 9" stroke="#f5b400" stroke-width="1.6"/>
        <path d="M58 20v8M54 24h8" stroke="#f5b400" stroke-width="1.6"/>
      </svg>
      <h3 class="step__title">Signup To Begin</h3>
      <p class="step__body">In order to get the full experience you need to sign<br>up. It takes only 30 seconds!<br>Hurry up, we have a big sorprise to you after that.</p>
    </div>

    <div class="step step--interests">
      <svg class="step__icon" width="66" height="64" viewBox="0 0 66 64" fill="none">
        <path d="M56 12A30 30 0 1 0 61 26" stroke="#474c51" stroke-width="1.6"/>
        <path d="M30 44l-9-9a5.5 5.5 0 0 1 9-6 5.5 5.5 0 0 1 9 6z" stroke="#f5b400" stroke-width="1.8" stroke-linejoin="round"/>
        <path d="M53 21l3 3 6-7" stroke="#f5b400" stroke-width="1.6"/>
      </svg>
      <h3 class="step__title">Tell us your interests</h3>
      <p class="step__body">We will craft an ongoing stream of exclusive offers<br>just for you. You no longer have to follow links and<br>hunt down the great new deals on the store.</p>
    </div>
  </section>

  <section class="experience">
    <h2 class="experience__title">Broaden your shopping experience</h2>
    <p class="experience__body">Find out what's trending in your area and<br>share your shopping experience with other<br>users.<br>Because your opinion matters!</p>
    <div class="video" role="img" aria-label="Video still: hands holding a tablet at a café table beside a phone and a glass">
      <div class="video__play">
        <svg width="22" height="24" viewBox="0 0 22 24"><path d="M2 1l19 11L2 23z" fill="#fff"/></svg>
      </div>
    </div>
  </section>

  <section class="business">
    <div class="business__people">
      <div class="business__portrait business__portrait--left" role="img" aria-label="Photo of a smiling shop owner in a café"></div>
      <div class="business__portrait business__portrait--right" role="img" aria-label="Photo of a smiling shop owner"></div>
      <div class="business__portrait business__portrait--center" role="img" aria-label="Photo of a barista behind a café counter"></div>
    </div>
    <h2 class="business__title">Business Users</h2>
    <p class="business__body">At TrindaMo, we help businesses reach their<br>customers by matching interests in products &amp;<br>services. If your products &amp; services match<br>with the interests of your target market, you</p>
  </section>
</body>
</html>
```